TalkWell Needs a Business Card

We need a business card for Tomas Ferreby, Ph.D., CCC-SLP, who is affiliated with Hollander Ridge University. He is an Associate Professor and Licensed Speech-Language Pathologist, Department of Communication Disorders, College of Health and Human Services.

He has a consulting business "TalkWell Consultant". The logo is attached. The consulting company color is Turquoise. HRU school color is orange.

The consulting business focus on: Consultation, Research & Professional Development. Our target market is individuals with annual family income of $100,000.00 or more for consultation and speech-language pathologists for professional development activities.

No harsh colors, subtle colors appreciated. Address, e-mail, telephone, and small scan logo for a link to our website. Creativity in design will be appreciated. Please add your comments, why you created this design?

Thanks and looking for submissions.

```html
<!DOCTYPE html>
<html lang="en">
<head>
<meta charset="utf-8">
<title>TalkWell Consultant – Business Card</title>
<link rel="stylesheet" href="https://fonts.googleapis.com/css2?family=Noto+Sans:wght@400;700&display=swap">
<style>
  :root {
    --stage: #b9b5bc;
    --card: #ffffff;
    --turquoise: #5bc6cc;
    --green: #4cb848;
    --bar: #6a6a6c;
    --ink: #5b5b5d;
    --ink-dark: #3e3e40;
    --bar-text: #f2f2f2;
  }
  * { margin: 0; padding: 0; box-sizing: border-box; }
  html, body { width: 1200px; height: 900px; overflow: hidden; }
  body {
    background: var(--stage);
    font-family: "Noto Sans", Arial, sans-serif;
    position: relative;
  }
  .card {
    position: absolute;
    top: 302px;
    width: 520px;
    height: 296px;
    background: var(--card);
    overflow: hidden;
    box-shadow: 0 2px 6px rgba(0,0,0,0.25);
  }
  .card--front { left: 50px; }
  .card--back { left: 630px; }

  /* Front */
  .brand {
    position: absolute;
    left: 80px;
    top: 50%;
    transform: translateY(-50%);
    display: flex;
    align-items: center;
    gap: 18px;
  }
  .brand__dot {
    width: 64px;
    height: 64px;
    border-radius: 50%;
    background: var(--turquoise);
  }
  .brand__name {
    color: var(--turquoise);
    font-size: 34px;
    font-weight: 400;
    line-height: 1.15;
  }

  /* Back */
  .side-band {
    position: absolute;
    left: 0;
    top: 0;
    width: 104px;
    height: 100%;
  }
  .holder-name {
    position: absolute;
    left: 236px;
    right: 14px;
    top: 42px;
    color: var(--ink);
    font-size: 34px;
    font-weight: 400;
    line-height: 1.2;
    white-space: nowrap;
  }
  .credential-bar {
    position: absolute;
    left: 230px;
    right: -10px;
    top: 96px;
    height: 44px;
    background: var(--bar);
    border-radius: 4px 0 0 4px;
    padding: 5px 8px;
    color: var(--bar-text);
    font-size: 12.5px;
    line-height: 1.35;
  }
  .contact {
    position: absolute;
    right: 14px;
    bottom: 16px;
    text-align: right;
    color: var(--ink);
    font-style: normal;
    line-height: 1.2;
  }
  .contact__address { font-size: 14px; }
  .contact__phone { font-size: 20px; }
  .contact__email { font-size: 14px; }
  .contact__web { font-size: 14px; font-weight: 700; color: var(--ink-dark); }
</style>
</head>
<body>
  <section class="card card--front" aria-label="Card front">
    <div class="brand">
      <span class="brand__dot"></span>
      <span class="brand__name">TalkWell<br>Consultant</span>
    </div>
  </section>

  <section class="card card--back" aria-label="Card back">
    <svg class="side-band" viewBox="0 0 104 296" preserveAspectRatio="none" aria-hidden="true">
      <path d="M0 0 H104 V296 H0 Z" fill="var(--turquoise)"/>
    </svg>
    <h1 class="holder-name">Tomas Ferreby</h1>
    <p class="credential-bar">Ph.D.&nbsp; CCC-SLP affiliated with<br>Hollander Ridge University</p>
    <address class="contact">
      <div class="contact__address">Building#,Street #, City</div>
      <div class="contact__phone">000 000 000</div>
      <div class="contact__email">email@web.com</div>
      <div class="contact__web">www.web.com</div>
    </address>
  </section>
</body>
</html>
```